Varnholt Works 'Ember Glaze' Label

We need a label for our new Exterior Ceramic Coat spray. It is going to be called Ember Glaze. This label needs to exude a premium feel yet also retain elements of FUN. This product when applied to a vehicle exterior creates a highly durable barrier and incredible shine. Ceramic coats are a popular way to make your paint turn heads! - and ours is the best. We'd like to see designs that match our line and previous projects but we want this label to stick out a little like its something special. Oranges, Reds, Silver, White, could all be great ideas, we dont have a set color or fragrance for this yet so all ideas are welcome!

```html
<!DOCTYPE html>
<html lang="en">
<head>
<meta charset="utf-8">
<title>Ember Glaze – Exterior Ceramic Coat Spray Label</title>
<link href="https://fonts.googleapis.com/css2?family=Cabin:wght@500;600;700&display=swap" rel="stylesheet">
<style>
  :root {
    --backdrop: #9a9ca3;
    --label-white: #f4f3f3;
    --ember-red: #8a1a24;
    --ember-deep: #6e111a;
    --ember-soft: #b7545c;
    --ink: #2b2b2d;
    --ink-soft: #55575b;
  }
  * { box-sizing: border-box; margin: 0; padding: 0; }
  html, body {
    width: 1200px;
    height: 855px;
    overflow: hidden;
    background: var(--backdrop);
  }
  .canvas {
    position: relative;
    width: 1200px;
    height: 855px;
    display: flex;
    align-items: center;
    justify-content: center;
  }
  .label {
    position: relative;
    width: 460px;
    height: 790px;
    background: var(--label-white);
    overflow: hidden;
    font-family: "Cabin", "Gill Sans", sans-serif;
    color: var(--ink);
  }
  .label__marble {
    position: absolute;
    inset: 0;
    background:
      radial-gradient(ellipse 60% 18% at 30% 12%, var(--label-white) 0 35%, transparent 70%),
      radial-gradient(ellipse 50% 20% at 75% 58%, var(--ember-soft) 0 30%, transparent 75%),
      radial-gradient(ellipse 55% 14% at 25% 90%, var(--label-white) 0 30%, transparent 70%),
      linear-gradient(160deg, var(--ember-red) 0%, var(--ember-deep) 30%, var(--ember-soft) 55%, var(--ember-red) 75%, var(--ember-deep) 100%);
  }
  .band {
    position: absolute;
    left: 0;
    right: 0;
    display: flex;
    flex-direction: column;
    align-items: center;
    justify-content: center;
    text-align: center;
    background: linear-gradient(to bottom,
      rgba(244,243,243,0) 0%,
      var(--label-white) 22%,
      var(--label-white) 78%,
      rgba(244,243,243,0) 100%);
  }
  .band--title { top: 280px; height: 140px; }
  .band--claims { top: 505px; height: 150px; }
  .product-name {
    font-weight: 700;
    font-size: 40px;
    letter-spacing: 1.5px;
    line-height: 1;
    color: var(--ink);
  }
  .product-name__accent { color: var(--ink-soft); }
  .product-type {
    margin-top: 12px;
    font-weight: 600;
    font-size: 21px;
    color: var(--ink);
  }
  .claims {
    list-style: none;
    font-weight: 600;
    font-size: 25px;
    line-height: 1.45;
  }
  .volume {
    position: absolute;
    left: 50%;
    top: 695px;
    transform: translate(-50%, -50%);
    width: 150px;
    height: 62px;
    border-radius: 50%;
    background: radial-gradient(ellipse at center, var(--label-white) 55%, rgba(244,243,243,0) 100%);
    display: flex;
    align-items: center;
    justify-content: center;
    font-weight: 600;
    font-size: 20px;
  }
</style>
</head>
<body>
  <main class="canvas">
    <section class="label">
      <div class="label__marble" role="img" aria-label="Marbled swirl pattern in deep red and white"></div>

      <header class="band band--title">
        <h1 class="product-name">EMBER <span class="product-name__accent">GLAZE</span></h1>
        <p class="product-type">Exterior Ceramic Coat spray</p>
      </header>

      <div class="band band--claims">
        <ul class="claims">
          <li>highly durable barrier</li>
          <li>incredible shine</li>
        </ul>
      </div>

      <p class="volume">200ml</p>
    </section>
  </main>
</body>
</html>
```